SIGN UP PAGE AND CHECK OUT PROCESS DESIGN NEEDED

I offer a subscription service. Two products that offer the same exact features just two different prices as the cheaper product offers limited of all the features....<br/><br/>PLEASE USE EXISTING THEME OF CURRENT DESIGN JUST MAKE AN IMPROVED SIGN UP PAGE. <br/><br/><br/>NEED SIGN UP PAGE for a subscription service..... <br/>This is my current sign up page, only offers one product: https://www.brightpromoperks.example/?page=signup <br/><br/>Please use all the same fields and content listed on this sign up page also please do a fake sign up to see the credit card page. I also need the credit card page to be designed....or if you want to combine the sign up and credit card page, etc. all in one I am open for that too....my goal is a super quick an easy sign up for customer. <br/><br/> AL A CARTE PROGRAM<br/>1 CERTIFICATE TYPE EACH MONTH<br/>$49/MTH MONTH TO MONTH BASIS NO CONTRACTS<br/>$239 ONE TIME PAYMENT FOR 6 MTHS OF SERVICE<br/>$399 ONE TIME PAYMENT FOR 12 MONTHS OF SERVICE<br/><br/>FEATURES:<br/><br/>UNLIMITED CERTIFICATE PDF DOWNLOADS<br/><br/>UNLIMITED E-MAIL CERTIFICATES<br/><br/>UNLIMITED TEXT/SMS CERTIFICATES<br/><br/>UNLIMITED API USAGE<br/><br/>UNLIMITED WEB BANNER CERTIFICATES<br/><br/>FULL REDEMPTION TRACKING<br/><br/>CERTIFICATE DISTRIBUTION REPORTS<br/><br/>WHITE LABEL REDEMPTION SITE<br/><br/>END USER MARKETING VIDEOS<br/><br/>MARKETING POSTERS AND FLYERS<br/><br/>PRODUCT DESCRIPTIONI BROCHURES<br/><br/>THE LATEST TIPS<br/><br/>SEPERATE REDEMPTION WEBSITES<br/><br/>CONTACT US 24/7<br/><br/>AFFILIATE PROGRAM<br/><br/>DISCOUNT TRAVEL BOOKING ENGINE<br/><br/>UNLIMITED PROGRAM<br/>UNLIMITED AMOUNTS OF ALL THE CERTIFICATES<br/>$99/MTH MONTH TO MONTH BASIS NO CONTRACTS<br/>$495 ONE TIME PAYMENT FOR 6 MTHS OF SERVICE<br/>$2,295 ONE TIME PAYMENT FOR 12 MONTHS OF SERVICE<br/><br/>FEATURES:<br/><br/>UNLIMITED CERTIFICATE PDF DOWNLOADS<br/><br/>UNLIMITED E-MAIL CERTIFICATES<br/><br/>UNLIMITED TEXT/SMS CERTIFICATES<br/><br/>UNLIMITED API USAGE<br/><br/>UNLIMITED WEB BANNER CERTIFICATES<br/><br/>FULL REDEMPTION TRACKING<br/><br/>CERTIFICATE DISTRIBUTION REPORTS<br/><br/>WHITE LABEL REDEMPTION SITE<br/><br/>END USER MARKETING VIDEOS<br/><br/>MARKETING POSTERS AND FLYERS<br/><br/>PRODUCT DESCRIPTIONI BROCHURES<br/><br/>THE LATEST TIPS<br/><br/>SEPERATE REDEMPTION WEBSITES<br/><br/>CONTACT US 24/7<br/><br/>AFFILIATE PROGRAM<br/><br/>DISCOUNT TRAVEL BOOKING ENGINE<br/><br/><br/>

Target Market(s)

B2B SMALL BUSINESS OWNERS
MARKETERS
ADVERTISERS

Industry/Entity Type

Digital Marketing

Number of Pages Required

3 page

Colors

Designer to choose colors to be used in the design.

Requirements
Must have
• MUST MATCH EXISTING THEME
Nice to have
• A VERY MODERN DESIGN

```html
<!DOCTYPE html>
<html lang="en">
<head>
<meta charset="utf-8">
<title>Sign Up – Select Your Plan</title>
<link href="https://fonts.googleapis.com/css2?family=Raleway:wght@400;500;700;800;900&family=Lato:wght@300;400;700&display=swap" rel="stylesheet">
<style>
:root{
  --ink:#4d5059;
  --blue:#0a74c7;
  --blue-dark:#0661a8;
  --slate:#535761;
  --band:#262a30;
  --card:#f5f5f6;
  --orange:#f8a702;
  --orange-dark:#d98f00;
  --red:#f4511e;
  --white:#ffffff;
}
*{box-sizing:border-box;margin:0;padding:0}
html,body{width:790px;height:1200px;overflow:hidden;background:var(--white)}
body{position:relative;font-family:"Raleway",sans-serif;color:var(--ink)}

.hero-icon{position:absolute;left:356px;top:34px;width:78px;height:78px}
.hero-title{position:absolute;top:124px;left:0;width:790px;text-align:center;font-weight:700;font-size:20.5px;line-height:29px;letter-spacing:-.1px}
.hero-title .accent{color:var(--blue)}
.rule{position:absolute;left:363px;width:64px;height:2px;background:var(--blue)}

.features{position:absolute;top:229px;left:0;width:790px;height:242px;color:var(--white)}
.features-bg{position:absolute;inset:0;background:radial-gradient(ellipse at 35% 55%,#3a3f47 0%,#2a2e34 45%,#1f2226 100%)}
.features-title{position:relative;text-align:center;font-weight:700;font-size:13.6px;line-height:21px;padding-top:36px}
.feature-list{position:absolute;top:94px;list-style:none;font-weight:700;font-size:9.3px;line-height:19px}
.feature-list li{display:flex;align-items:center;gap:3px;white-space:nowrap}
.feature-list svg{width:10px;height:8px;flex:none}

.plans-title{position:absolute;top:506px;left:0;width:790px;text-align:center;font-weight:700;font-size:20.5px}
.plans-title .accent{color:var(--blue)}

.plan{position:absolute;top:576px;width:325px}
.plan-a{left:66px}.plan-u{left:399px}
.plan-head{height:71px;color:var(--white);text-align:center;padding-top:12px}
.plan-a .plan-head{background:var(--slate)}
.plan-u .plan-head{background:var(--blue)}
.plan-name{font-weight:700;font-size:20px;line-height:24px}
.plan-sub{display:flex;justify-content:center;align-items:center;gap:6px;font-size:14px;font-weight:400;margin-top:4px}
.plan-sub::before,.plan-sub::after{content:"";width:25px;height:1px;background:var(--white)}

.tier{position:absolute;left:0;width:325px}
.tab{position:absolute;left:15px;top:0;width:80px;height:23px;border-radius:4px 4px 0 0;color:var(--white);font-weight:700;font-size:9.8px;text-align:center;line-height:23px}
.plan-a .tab{background:var(--slate)}
.plan-u .tab{background:var(--blue)}
.save{position:absolute;left:95px;top:5px;height:14px;padding:0 5px;background:var(--red);color:var(--white);font-weight:800;font-size:7.5px;line-height:14px}
.card{position:absolute;top:23px;left:0;width:325px;height:106px;background:var(--card);border-radius:3px;display:flex}
.card-parts{width:215px;position:relative}
.card-total{flex:1;border-left:2px solid var(--white);text-align:center}
.price{position:absolute;top:8px;width:70px;text-align:center;font-weight:800;font-size:28px;line-height:38px;color:var(--ink);border-bottom:1px solid #e0e0e2;padding-bottom:6px}
.price.recurring{left:17px}.price.setup{left:127px}
.plus{position:absolute;left:98px;top:15px;font-weight:800;font-size:20px}
.note{position:absolute;top:63px;width:90px;text-align:center;font-family:"Lato",sans-serif;font-weight:300;font-size:8.3px;line-height:10.5px;color:#555}
.note.recurring{left:7px}.note.setup{left:117px}
.note sup{color:var(--blue);font-weight:700;font-size:8px}
.total{font-weight:800;font-size:28px;color:var(--blue);line-height:38px;margin-top:8px}
.select{display:inline-flex;align-items:center;justify-content:space-between;width:89px;height:29px;margin-top:8px;padding:0 7px 0 17px;background:var(--orange);border-bottom:2px solid var(--orange-dark);border-radius:2px;color:var(--white);font-weight:800;font-size:10px;letter-spacing:.2px}
.select svg{width:11px;height:11px}

.footnote{position:absolute;top:1097px;left:0;width:790px;text-align:center;font-family:"Lato",sans-serif;font-size:6.4px;color:var(--blue)}
</style>
</head>
<body>

<svg class="hero-icon" viewBox="0 0 78 78" aria-hidden="true">
  <circle cx="39" cy="39" r="39" fill="#d9d9d9"/>
  <circle cx="39" cy="39" r="35" fill="var(--blue)"/>
  <g fill="none" stroke="#fff" stroke-width="2.2" stroke-linejoin="round" stroke-linecap="round">
    <rect x="22" y="35" width="8" height="18" rx="1"/>
    <path d="M30 36 l7-10 v-5 a3 3 0 0 1 5 1 v10 h9 a3 3 0 0 1 0 6 a3 3 0 0 1 0 5 a3 3 0 0 1 -1 5 a3 3 0 0 1 -2 5 h-18"/>
    <path d="M37 15 v-3 M44 17 l2-3 M30 17 l-2-3"/>
  </g>
</svg>

<h1 class="hero-title">CONGRATULATIONS ON MAKING THE DECISION TO<br><span class="accent">MAKE MORE MONEY FOR YOUR BUSINESS</span></h1>
<div class="rule" style="top:186px"></div>

<section class="features">
  <div class="features-bg" role="img" aria-label="Dark photo of a laptop keyboard on a desk"></div>
  <h2 class="features-title">THIS PROGRAM IS AN ONLINE SUBSCRIPTION BASED INCENTIVE MARKETING SYSTEM<br>WITH THE FOLLOWING FEATURES</h2>
  <ul class="feature-list" style="left:66px">
    <li><svg viewBox="0 0 10 8"><path d="M1 4 l3 3 l5-6" stroke="#1a8fe0" stroke-width="2" fill="none"/></svg>Unlimited Certificate PDF downloads</li>
    <li><svg viewBox="0 0 10 8"><path d="M1 4 l3 3 l5-6" stroke="#1a8fe0" stroke-width="2" fill="none"/></svg>Unlimited API usage</li>
    <li><svg viewBox="0 0 10 8"><path d="M1 4 l3 3 l5-6" stroke="#1a8fe0" stroke-width="2" fill="none"/></svg>Certificate Distribution Reports</li>
    <li><svg viewBox="0 0 10 8"><path d="M1 4 l3 3 l5-6" stroke="#1a8fe0" stroke-width="2" fill="none"/></svg>Marketing Posters and Flyers</li>
    <li><svg viewBox="0 0 10 8"><path d="M1 4 l3 3 l5-6" stroke="#1a8fe0" stroke-width="2" fill="none"/></svg>Discount Travel Booking Engine</li>
  </ul>
  <ul class="feature-list" style="left:316px">
    <li><svg viewBox="0 0 10 8"><path d="M1 4 l3 3 l5-6" stroke="#1a8fe0" stroke-width="2" fill="none"/></svg>Unlimited E-mail Certificates</li>
    <li><svg viewBox="0 0 10 8"><path d="M1 4 l3 3 l5-6" stroke="#1a8fe0" stroke-width="2" fill="none"/></svg>Unlimited Web Banner Certificates</li>
    <li><svg viewBox="0 0 10 8"><path d="M1 4 l3 3 l5-6" stroke="#1a8fe0" stroke-width="2" fill="none"/></svg>White Label Redemption Site</li>
    <li><svg viewBox="0 0 10 8"><path d="M1 4 l3 3 l5-6" stroke="#1a8fe0" stroke-width="2" fill="none"/></svg>Product Description Brochures</li>
    <li><svg viewBox="0 0 10 8"><path d="M1 4 l3 3 l5-6" stroke="#1a8fe0" stroke-width="2" fill="none"/></svg>Affiliate Program</li>
    <li><svg viewBox="0 0 10 8"><path d="M1 4 l3 3 l5-6" stroke="#1a8fe0" stroke-width="2" fill="none"/></svg>Contact Us 24/7</li>
  </ul>
  <ul class="feature-list" style="left:561px">
    <li><svg viewBox="0 0 10 8"><path d="M1 4 l3 3 l5-6" stroke="#1a8fe0" stroke-width="2" fill="none"/></svg>Unlimited Text/SMS Certificates</li>
    <li><svg viewBox="0 0 10 8"><path d="M1 4 l3 3 l5-6" stroke="#1a8fe0" stroke-width="2" fill="none"/></svg>Full Redemption Tracking</li>
    <li><svg viewBox="0 0 10 8"><path d="M1 4 l3 3 l5-6" stroke="#1a8fe0" stroke-width="2" fill="none"/></svg>End User Marketing Videos</li>
    <li><svg viewBox="0 0 10 8"><path d="M1 4 l3 3 l5-6" stroke="#1a8fe0" stroke-width="2" fill="none"/></svg>Separate Redemption Websites</li>
    <li><svg viewBox="0 0 10 8"><path d="M1 4 l3 3 l5-6" stroke="#1a8fe0" stroke-width="2" fill="none"/></svg>The Latest Tips</li>
  </ul>
</section>

<h2 class="plans-title">SELECT YOUR <span class="accent">PREFERRED PLAN</span></h2>
<div class="rule" style="top:540px"></div>

<section class="plan plan-a">
  <header class="plan-head"><div class="plan-name">A LA CARTE PLAN</div><div class="plan-sub">1 Certificate Type Each Month</div></header>

  <div class="tier" style="top:94px">
    <div class="tab">MONTHLY</div>
    <div class="card">
      <div class="card-parts"><div class="price recurring">$49</div><div class="plus">+</div><div class="price setup">$99</div>
        <div class="note recurring">Charged every<sup>*</sup><br>30 days</div><div class="note setup">One-time<br>Set-up fee</div></div>
      <div class="card-total"><div class="total">$148</div><span class="select">SELECT<svg viewBox="0 0 12 12"><circle cx="6" cy="6" r="6" fill="#fff"/><path d="M5 3.5 l2.5 2.5 l-2.5 2.5" stroke="var(--orange)" stroke-width="1.6" fill="none"/></svg></span></div>
    </div>
  </div>

  <div class="tier" style="top:234px">
    <div class="tab">BI-ANNUAL</div><div class="save">SAVE 15%</div>
    <div class="card">
      <div class="card-parts"><div class="price recurring">$249</div><div class="plus">+</div><div class="price setup">$99</div>
        <div class="note recurring">Charged every<sup>*</sup><br>6 months</div><div class="note setup">One-time<br>Set-up fee</div></div>
      <div class="card-total"><div class="total">$348</div><span class="select">SELECT<svg viewBox="0 0 12 12"><circle cx="6" cy="6" r="6" fill="#fff"/><path d="M5 3.5 l2.5 2.5 l-2.5 2.5" stroke="var(--orange)" stroke-width="1.6" fill="none"/></svg></span></div>
    </div>
  </div>

  <div class="tier" style="top:373px">
    <div class="tab">ANNUAL</div><div class="save">SAVE 32%</div>
    <div class="card">
      <div class="card-parts"><div class="price recurring">$399</div><div class="plus">+</div><div class="price setup">$99</div>
        <div class="note recurring">Charged every<sup>*</sup><br>12 months</div><div class="note setup">One-time<br>Set-up fee</div></div>
      <div class="card-total"><div class="total">$498</div><span class="select">SELECT<svg viewBox="0 0 12 12"><circle cx="6" cy="6" r="6" fill="#fff"/><path d="M5 3.5 l2.5 2.5 l-2.5 2.5" stroke="var(--orange)" stroke-width="1.6" fill="none"/></svg></span></div>
    </div>
  </div>
</section>

<section class="plan plan-u">
  <header class="plan-head"><div class="plan-name">UNLIMITED PLAN</div><div class="plan-sub">Unlimited Certificate Types</div></header>

  <div class="tier" style="top:94px">
    <div class="tab">MONTHLY</div>
    <div class="card">
      <div class="card-parts"><div class="price recurring">$99</div><div class="plus">+</div><div class="price setup">$99</div>
        <div class="note recurring">Charged every<sup>*</sup><br>30 days</div><div class="note setup">One-time<br>Set-up fee</div></div>
      <div class="card-total"><div class="total">$198</div><span class="select">SELECT<svg viewBox="0 0 12 12"><circle cx="6" cy="6" r="6" fill="#fff"/><path d="M5 3.5 l2.5 2.5 l-2.5 2.5" stroke="var(--orange)" stroke-width="1.6" fill="none"/></svg></span></div>
    </div>
  </div>

  <div class="tier" style="top:234px">
    <div class="tab">BI-ANNUAL</div><div class="save">SAVE 16%</div>
    <div class="card">
      <div class="card-parts"><div class="price recurring">$499</div><div class="plus">+</div><div class="price setup">$99</div>
        <div class="note recurring">Charged every<sup>*</sup><br>6 months</div><div class="note setup">One-time<br>Set-up fee</div></div>
      <div class="card-total"><div class="total">$598</div><span class="select">SELECT<svg viewBox="0 0 12 12"><circle cx="6" cy="6" r="6" fill="#fff"/><path d="M5 3.5 l2.5 2.5 l-2.5 2.5" stroke="var(--orange)" stroke-width="1.6" fill="none"/></svg></span></div>
    </div>
  </div>

  <div class="tier" style="top:373px">
    <div class="tab">ANNUAL</div><div class="save">SAVE 33%</div>
    <div class="card">
      <div class="card-parts"><div class="price recurring">$799</div><div class="plus">+</div><div class="price setup">$99</div>
        <div class="note recurring">Charged every<sup>*</sup><br>12 months</div><div class="note setup">One-time<br>Set-up fee</div></div>
      <div class="card-total"><div class="total">$898</div><span class="select">SELECT<svg viewBox="0 0 12 12"><circle cx="6" cy="6" r="6" fill="#fff"/><path d="M5 3.5 l2.5 2.5 l-2.5 2.5" stroke="var(--orange)" stroke-width="1.6" fill="none"/></svg></span></div>
    </div>
  </div>
</section>

<p class="footnote"><sup>*</sup>You must submit a support ticket from your back end account at least 3 business days before your next billing date in order not be charged for the following cycle.</p>

</body>
</html>
```